Logo, homepage, and product page design cleaning equipment

Looking for a logo, homepage, and product page design for our cartwell store. We sell cleaning equipment that serves the auto detailing industry. I have attached a picture of our main product. The company is called Brisk Cleaning Equipment with a slogan of The Way to Clean (slogan incorporated is optional). A site I really like is https://www.harborlanternroast.example/. It has a very clean layout and very clear on their messaging.

Target Market(s)

Auto detailing industry

Industry/Entity Type

Automotive

Logo Text

Brisk Cleaning Equipment

Font styles to use
Serif
Sans Serif

Requirements
Must have
• A nice clean layout. Not too busy. Easy to navigate.
Nice to have
• consistency in colors. Appeal to people who care about their cars. They have an eye for detail.
Should not have
• It cannot be too busy.

```html
<!DOCTYPE html>
<html lang="en">
<head>
<meta charset="utf-8">
<title>Brisk Cleaning Equipment</title>
<link href="https://fonts.googleapis.com/css2?family=Lato:wght@400;700&family=Oswald:wght@500;600&display=swap" rel="stylesheet">
<style>
:root{
  --red:#c8283a;
  --blue:#03a9f4;
  --ink:#222;
  --text:#444;
  --muted:#999;
  --panel:#ececec;
  --panel-dark:#e6e6e6;
  --card:#f4f4f4;
  --white:#fff;
}
*{margin:0;padding:0;box-sizing:border-box}
html,body{width:1200px;height:3782px;overflow:hidden}
body{position:relative;background:var(--white);font-family:'Lato',sans-serif;color:var(--text)}
.abs{position:absolute}
.heading{font-family:'Oswald',sans-serif;font-weight:500;color:var(--ink);text-transform:uppercase;letter-spacing:1px}
.btn{position:absolute;background:var(--red);color:var(--white);font-size:14px;text-transform:uppercase;letter-spacing:.5px;display:flex;align-items:center;justify-content:center;border-radius:2px}
.section-title{position:absolute;left:0;width:1200px;text-align:center;font-size:32px}
.rule{position:absolute;left:572px;width:56px;height:3px;background:var(--blue)}
.media{position:absolute}

/* header */
.topbar{position:absolute;left:0;top:0;width:1200px;height:151px;background:#f6f6f6}
.util{position:absolute;top:16px;font-size:14px;color:var(--text);display:flex;align-items:center;gap:8px}
.logo{position:absolute;left:480px;top:12px;width:240px;text-align:center}
.logo-mark{width:36px;height:36px;background:var(--red);margin:0 auto 5px;border-radius:4px}
.logo-name{font-size:14px;font-weight:700;color:var(--blue);line-height:16px}
.logo-tag{font-size:9px;color:var(--text);line-height:12px}
.nav a{position:absolute;top:116px;font-size:14px;color:var(--text);text-decoration:none}
.nav .active{color:var(--blue);border-bottom:2px solid var(--blue);padding-bottom:3px}

/* hero */
.hero{position:absolute;left:0;top:151px;width:1200px;height:517px;background:#f6f6f6}
.hero-copy{position:absolute;right:111px;top:100px;text-align:right}
.hero-copy .kicker{font-size:32px;line-height:40px}
.hero-copy .big{font-size:46px;line-height:56px;letter-spacing:2px}

/* promos */
.promo{position:absolute;top:668px;height:681px}
.promo h3{position:absolute;top:428px;width:100%;text-align:center;font-size:32px}
.promo p{position:absolute;top:477px;left:50%;width:240px;margin-left:-120px;text-align:center;font-size:14px;line-height:19px}

/* products */
.tabs span{position:absolute;top:1522px;font-size:14px;color:var(--text)}
.tabs .on{color:var(--blue)}
.product{position:absolute;top:1588px;width:202px;height:265px;background:var(--card)}
.product-hover{background:var(--red)}
.p-name{position:absolute;top:1868px;width:202px;text-align:center;font-size:14px;color:var(--ink)}
.p-price{position:absolute;top:1888px;width:202px;text-align:center;font-size:15px;font-weight:700;color:var(--blue)}

/* about */
.about{position:absolute;left:0;top:2105px;width:1200px;height:441px;background:linear-gradient(120deg,#dcdcdc,#efefef 50%,#d6d6d6)}
.about-copy{position:absolute;left:245px;top:2262px;width:710px;text-align:center;font-size:14px;line-height:20px;color:var(--text)}

/* news */
.news{position:absolute;top:2728px;width:265px;height:360px;background:var(--card)}
.news .media{left:0;top:0;width:265px;height:184px}
.news h4{position:absolute;left:18px;top:200px;font-size:15px;font-weight:700;color:var(--ink)}
.news .meta{position:absolute;left:18px;top:228px;font-size:12px;color:var(--muted)}
.news p{position:absolute;left:18px;top:252px;width:230px;font-size:14px;line-height:19px;color:var(--text)}
.news a{position:absolute;left:18px;top:318px;font-size:12px;color:var(--red);text-decoration:underline}

/* features */
.feature{position:absolute;top:3285px;width:245px;height:71px;border:1px solid #ddd;display:flex;align-items:center;gap:14px;padding-left:40px}
.feature b{display:block;font-family:'Oswald',sans-serif;font-weight:500;font-size:18px;color:var(--ink)}
.feature small{font-size:11px;color:var(--text)}

/* footer */
.footer{position:absolute;left:0;top:3416px;width:1200px;height:366px;background:var(--blue);color:var(--white)}
.footer h5{position:absolute;top:66px;font-family:'Oswald',sans-serif;font-weight:500;font-size:20px}
.footer ul{position:absolute;list-style:none;font-size:14px;line-height:24px}
.footer li::before{content:"\203A";margin-right:6px}
.contact-row{position:absolute;left:509px;font-size:14px;display:flex;gap:8px;align-items:flex-start}
.social span{display:inline-block;width:16px;height:16px;border:1.5px solid var(--white);border-radius:50%;margin-right:5px}
.pay span{display:inline-block;width:32px;height:20px;background:var(--white);margin-left:6px;border-radius:2px}
.copyright{position:absolute;left:121px;top:284px;font-size:13px}
</style>
</head>
<body>

<header class="topbar">
  <div class="util" style="left:121px">
    <svg width="14" height="14" viewBox="0 0 14 14"><circle cx="6" cy="6" r="4.5" fill="none" stroke="#444" stroke-width="1.5"/><line x1="9.5" y1="9.5" x2="13" y2="13" stroke="#444" stroke-width="1.5"/></svg>Search
  </div>
  <div class="logo">
    <div class="logo-mark"></div>
    <div class="logo-name">Brisk Cleaning Equipment</div>
    <div class="logo-tag">The Way to Clean</div>
  </div>
  <div class="util" style="left:888px">
    <svg width="14" height="14" viewBox="0 0 14 14"><circle cx="7" cy="4.5" r="3" fill="none" stroke="#444" stroke-width="1.3"/><path d="M1.5 13.5c0-3 2.5-5 5.5-5s5.5 2 5.5 5" fill="none" stroke="#444" stroke-width="1.3"/></svg>Login / Register
  </div>
  <div class="util" style="left:1038px">
    <svg width="16" height="14" viewBox="0 0 16 14"><path d="M1 1h3l2 8h8l1.5-6H5" fill="none" stroke="#444" stroke-width="1.3"/><circle cx="7" cy="12" r="1.2" fill="#444"/><circle cx="13" cy="12" r="1.2" fill="#444"/></svg>(2)
  </div>
  <nav class="nav">
    <a class="active" style="left:444px">Home</a>
    <a style="left:512px">Shop</a>
    <a style="left:574px">About</a>
    <a style="left:647px">Blog</a>
    <a style="left:700px">Contact</a>
  </nav>
</header>

<section class="hero">
  <div class="media" role="img" aria-label="Front of a white compact car, half clean and half dirty" style="left:0;top:20px;width:592px;height:497px;background:linear-gradient(90deg,#e9e9e9,#cfcfcf 50%,#1f1f1f 50%,#2c2c2c 75%,#d8d8d8)"></div>
  <div class="hero-copy heading">
    <div class="kicker">Best Auto</div>
    <div class="big">Detailing &amp; Cleaning</div>
    <div class="big">Equipments</div>
  </div>
  <div class="btn" style="left:872px;top:283px;width:207px;height:58px">Shop Now</div>
</section>

<section class="promo" style="left:0;width:597px;background:var(--panel);border-right:1px solid #ddd">
  <div class="media" role="img" aria-label="Black pump foam sprayer bottle" style="left:222px;top:58px;width:150px;height:330px;background:linear-gradient(180deg,#3a3a3a,#111);border-radius:40px 40px 10px 10px"></div>
  <h3 class="heading">New Arrival</h3>
  <p>Lorem Ipsum is simply dummy text of the printing and typesetting industry.</p>
  <div class="btn" style="left:197px;top:535px;width:206px;height:58px">Shop Now</div>
</section>

<section class="promo" style="left:597px;width:603px;background:var(--panel-dark)">
  <div class="media" role="img" aria-label="Grey carpet extractor machine with hose" style="left:110px;top:60px;width:300px;height:330px;background:linear-gradient(180deg,#b5b5b5,#7d7d7d);border-radius:20px"></div>
  <h3 class="heading">Get Discount %</h3>
  <p>Lorem Ipsum is simply dummy text of the printing and typesetting industry.</p>
  <div class="btn" style="left:184px;top:535px;width:207px;height:58px">Shop Now</div>
</section>

<section>
  <h2 class="heading section-title" style="top:1418px">Feature Product</h2>
  <div class="rule" style="top:1484px"></div>
  <div class="tabs">
    <span class="on" style="left:440px">New Arrival</span>
    <span style="left:548px">Popular Products</span>
    <span style="left:688px">Best Selling</span>
  </div>

  <div class="product" style="left:192px">
    <div class="media" role="img" aria-label="Black pump foam sprayer" style="left:56px;top:30px;width:90px;height:200px;background:linear-gradient(180deg,#3a3a3a,#111);border-radius:24px 24px 6px 6px"></div>
  </div>
  <div class="product" style="left:400px">
    <div class="media" role="img" aria-label="Green pressure washer with lance" style="left:36px;top:20px;width:130px;height:225px;background:linear-gradient(180deg,#2f7a45,#1d4f2c);border-radius:12px"></div>
  </div>
  <div class="product product-hover" style="left:607px">
    <div class="media" role="img" aria-label="Pressure washer seen through red hover overlay" style="left:40px;top:25px;width:122px;height:215px;background:#b52434;border-radius:12px"></div>
    <div class="btn" style="left:21px;top:100px;width:160px;height:36px;background:var(--blue);font-size:13px">Add to cart</div>
    <svg class="abs" style="left:66px;top:144px" width="70" height="14" viewBox="0 0 70 14">
      <g fill="#f5c518">
        <path id="star" d="M7 0l2 4.6 5 .5-3.8 3.3 1.1 5L7 10.8 2.7 13.4l1.1-5L0 5.1l5-.5z"/>
        <use href="#star" x="14"/><use href="#star" x="28"/><use href="#star" x="42"/><use href="#star" x="56"/>
      </g>
    </svg>
  </div>
  <div class="product" style="left:812px">
    <div class="media" role="img" aria-label="Yellow and black pressure washer" style="left:46px;top:20px;width:110px;height:225px;background:linear-gradient(180deg,#f2d21b,#d9b400);border-radius:12px"></div>
  </div>

  <div class="p-name" style="left:192px">Product name</div><div class="p-price" style="left:192px">$ 420</div>
  <div class="p-name" style="left:400px">Product name</div><div class="p-price" style="left:400px">$ 1020</div>
  <div class="p-name" style="left:607px">Product name</div><div class="p-price" style="left:607px">$ 300</div>
  <div class="p-name" style="left:812px">Product name</div><div class="p-price" style="left:812px">$ 1150</div>

  <div class="btn" style="left:499px;top:1979px;width:204px;height:58px">View More</div>
</section>

<section class="about" role="img" aria-label="Soft grey photo of foam being sprayed on a car"></section>
<h2 class="heading section-title" style="top:2154px">About Us</h2>
<div class="rule" style="top:2220px"></div>
<p class="about-copy">Lorem Ipsum is simply dummy text of the printing and typesetting industry. Lorem Ipsum has been the industry's standard dummy text ever since the 1500s, when an unknown printer took a galley of type and scrambled it to make a type specimen book. It has survived not only five centuries, but also the leap into electronic typesetting, remaining essentially unchanged. It was popularised in the 1960s with the release of transfer sheets containing Lorem Ipsum passages, and more recently with desktop publishing software and layout tools including versions of Lorem Ipsum.</p>
<div class="btn" style="left:498px;top:2418px;width:206px;height:58px">Read More</div>

<section>
  <h2 class="heading section-title" style="top:2602px">Latest News</h2>
  <div class="rule" style="top:2668px"></div>

  <article class="news" style="left:189px">
    <div class="media" role="img" aria-label="Clean light leather car interior" style="background:linear-gradient(160deg,#6b6b6b,#d9d4cc)"></div>
    <h4>NEWS #1</h4>
    <div class="meta">Sep 9, 2018 &nbsp;&nbsp; Comments (13)</div>
    <p>Lorem Ipsum is simply dummy text of the printing and typesetting industry.</p>
    <a>Read More</a>
  </article>
  <article class="news" style="left:466px">
    <div class="media" role="img" aria-label="Yellow sponge washing a dark car surface" style="background:linear-gradient(160deg,#1e2a3a,#3b4a5e 60%,#d8b43a)"></div>
    <h4>NEWS # 2</h4>
    <div class="meta">Sep 9, 2018 &nbsp;&nbsp; Comments (13)</div>
    <p>Lorem Ipsum is simply dummy text of the printing and typesetting industry.</p>
    <a>Read More</a>
  </article>
  <article class="news" style="left:743px">
    <div class="media" role="img" aria-label="Glossy black car front in dark studio" style="background:linear-gradient(160deg,#0d0d0d,#3d3d3d)"></div>
    <h4>NEWS #3</h4>
    <div class="meta">Sep 9, 2018 &nbsp;&nbsp; Comments (13)</div>
    <p>Lorem Ipsum is simply dummy text of the printing and typesetting industry.</p>
    <a>Read More</a>
  </article>

  <div class="btn" style="left:498px;top:3146px;width:206px;height:58px">View More</div>
</section>

<section>
  <div class="feature" style="left:189px">
    <svg width="26" height="26" viewBox="0 0 26 26"><circle cx="13" cy="11" r="8" fill="none" stroke="#03a9f4" stroke-width="2"/><path d="M13 19v6" stroke="#03a9f4" stroke-width="2"/></svg>
    <div><b>Free Shipping</b><small>All Around The World</small></div>
  </div>
  <div class="feature" style="left:476px">
    <svg width="26" height="26" viewBox="0 0 26 26"><path d="M4 14a9 9 0 0 1 18 0v6h-4v-6h4M4 14v6h4v-6H4" fill="none" stroke="#03a9f4" stroke-width="2"/></svg>
    <div><b>Premium Support</b><small>24/7 Customer service</small></div>
  </div>
  <div class="feature" style="left:764px">
    <svg width="26" height="26" viewBox="0 0 26 26"><rect x="5" y="5" width="16" height="16" transform="rotate(45 13 13)" fill="none" stroke="#03a9f4" stroke-width="2"/><circle cx="13" cy="13" r="2.5" fill="#03a9f4"/></svg>
    <div><b>Payment Method</b><small>Cash On Delivery</small></div>
  </div>
</section>

<footer class="footer">
  <div class="abs" style="left:121px;top:60px;width:140px;text-align:center">
    <div style="width:36px;height:36px;background:var(--red);margin:0 auto 8px;border-radius:4px"></div>
    <div style="font-size:12px;font-weight:700">Brisk Cleaning Equipment</div>
  </div>
  <div class="abs" style="left:121px;top:150px;font-family:'Oswald',sans-serif;font-size:18px">Follow us on</div>
  <div class="abs social" style="left:121px;top:186px">
    <span></span><span></span><span></span><span></span><span></span><span></span>
  </div>

  <h5 style="left:343px">Quick Links</h5>
  <ul style="left:350px;top:112px">
    <li>Home</li><li>Shop</li><li>About</li><li>Blog</li><li>Contact</li>
  </ul>

  <h5 style="left:509px">Contact us</h5>
  <div class="contact-row" style="top:122px">
    <svg width="14" height="14" viewBox="0 0 14 14"><path d="M3 1l2.5 3-1.5 1.5a8 8 0 0 0 4.5 4.5L10 8.5l3 2.5-1.5 2.5C6 13 1 8 .5 2.5z" fill="#fff"/></svg>+010-555-0142
  </div>
  <div class="contact-row" style="top:166px">
    <svg width="14" height="14" viewBox="0 0 14 14"><rect x="1" y="3" width="12" height="8" fill="none" stroke="#fff" stroke-width="1.3"/><path d="M1 3l6 5 6-5" fill="none" stroke="#fff" stroke-width="1.3"/></svg>info@briskcleaningequipment.example
  </div>
  <div class="contact-row" style="top:210px">
    <svg width="14" height="16" viewBox="0 0 14 16"><path d="M7 15s5-5 5-9a5 5 0 0 0-10 0c0 4 5 9 5 9z" fill="#fff"/><circle cx="7" cy="6" r="2" fill="#03a9f4"/></svg>
    <span>215 Harbor Mill Rd.,<br>Eastfield, FL 32000</span>
  </div>

  <h5 style="left:802px">Newsletter</h5>
  <div class="abs" style="left:802px;top:130px;width:280px;font-size:14px;font-weight:700;line-height:19px">Lorem Ipsum is simply dummy text of the printing and typesetting industry.</div>
  <div class="abs" style="left:802px;top:198px;width:200px;height:44px;background:var(--white);color:var(--muted);font-size:12px;padding:14px 12px">Email Address</div>
  <div class="btn" style="left:1000px;top:198px;width:80px;height:44px;font-size:12px">Submit</div>

  <div class="abs" style="left:121px;top:264px;width:959px;height:1px;background:rgba(255,255,255,.4)"></div>
  <div class="copyright">CopyRight © 2018 Brisk Cleaning Equipment. All Right Reserve</div>
  <div class="abs pay" style="left:856px;top:281px">
    <span></span><span></span><span></span><span></span><span></span><span></span>
  </div>
</footer>

</body>
</html>
```